Business card design needed

Business Card design required for new small plumbing business.
Would like a logo/text look that is simple and unique and does not have to be representative of a plumbing company (ie. having a cartoon plumber or toilet etc) as the companyname is self explanatory.
Would like the main colour to be green (lime green).

Industry/Entity Type

Plumber

Contact Information for Business Card

BRISCOMB PLUMBING
ABN 61 947 205 318 004

Harold Tenfield
Licensed Plumber 71635
Phone: 0477 261 408

27 Worrell Drive,
Kelmsdale. 3862 Westmoor

Email: briscombplumbing@mailora.net

Logo Text

Briscomb Plumbing

Logo styles of interest
Character Logo
Wordmark Logo
Lettermark Logo

```html
<!DOCTYPE html>
<html lang="en">
<head>
<meta charset="utf-8">
<title>Briscomb Plumbing – Business Card</title>
<link rel="stylesheet" href="https://fonts.googleapis.com/css2?family=Jost:wght@700&family=Encode+Sans+Condensed:wght@400&family=Encode+Sans+Semi+Condensed:wght@400&display=swap">
<style>
  :root {
    --bg: #000000;
    --card-white: #ffffff;
    --lime: #6fab2b;
    --ink: #1a1a1a;
    --rule: #8a8a8a;
    --mark: #2c4f9e;
  }
  html, body {
    margin: 0;
    padding: 0;
    width: 1200px;
    height: 849px;
    overflow: hidden;
    background: var(--bg);
  }
  .canvas {
    position: relative;
    width: 1200px;
    height: 849px;
    background: var(--bg);
  }
  .card {
    position: absolute;
    border-radius: 12px;
    overflow: hidden;
  }
  .card--front {
    left: 109px; top: 290px;
    width: 466px; height: 266px;
    background: var(--card-white);
  }
  .card--back {
    left: 625px; top: 292px;
    width: 464px; height: 265px;
    background: var(--lime);
  }
  .card__band {
    position: absolute;
    left: 0; right: 0; bottom: 0;
    height: 15px;
  }
  .card--front .card__band { background: var(--lime); }
  .card--back .card__band { background: var(--card-white); }

  .contact {
    position: absolute;
    left: 233px; top: 15px;
    padding-left: 10px;
    border-left: 1px solid var(--rule);
    height: 146px;
    color: var(--ink);
  }
  .contact__name {
    margin: 0;
    font-family: "Encode Sans Condensed", "Arial Narrow", sans-serif;
    font-size: 18px;
    font-weight: 400;
    color: var(--lime);
    line-height: 20px;
  }
  .contact__role {
    margin: 0;
    font-family: "Encode Sans Condensed", "Arial Narrow", sans-serif;
    font-size: 10.5px;
    line-height: 13px;
  }
  .contact__details {
    margin: 37px 0 0;
    font-family: "Encode Sans Semi Condensed", "Arial Narrow", sans-serif;
    font-size: 11px;
    line-height: 15px;
    font-style: normal;
    white-space: nowrap;
  }

  .brand {
    position: absolute;
    display: flex;
    align-items: center;
    gap: 10px;
  }
  .brand__mark {
    flex: none;
    border-radius: 50%;
    background: var(--mark);
  }
  .brand__name {
    font-family: "Jost", "Futura", sans-serif;
    font-weight: 700;
    text-transform: uppercase;
    line-height: 0.95;
    letter-spacing: 0.2px;
  }
  .card--front .brand { left: 19px; top: 170px; }
  .card--front .brand__mark { width: 54px; height: 54px; }
  .card--front .brand__name { font-size: 34px; color: var(--ink); }

  .card--back .brand { left: 102px; top: 98px; }
  .card--back .brand__mark { width: 60px; height: 60px; }
  .card--back .brand__name { font-size: 35px; color: var(--card-white); }
</style>
</head>
<body>
<main class="canvas">
  <section class="card card--front" aria-label="Business card front">
    <div class="contact">
      <h1 class="contact__name">Harold Tenfield</h1>
      <p class="contact__role">Licensed Plumber 71635</p>
      <address class="contact__details">
        BRISCOMB PLUMBING ABN<br>
        61 947 205 318 004<br>
        Phone: 0477 261 408 27<br>
        Worrell Drive, Kelmsdale. 3862 Westmoor<br>
        Email: briscombplumbing@mailora.net
      </address>
    </div>
    <div class="brand">
      <span class="brand__mark" aria-hidden="true"></span>
      <span class="brand__name">Briscomb<br>Plumbing</span>
    </div>
    <div class="card__band"></div>
  </section>

  <section class="card card--back" aria-label="Business card back">
    <div class="brand">
      <span class="brand__mark" aria-hidden="true"></span>
      <span class="brand__name">Briscomb<br>Plumbing</span>
    </div>
    <div class="card__band"></div>
  </section>
</main>
</body>
</html>
```